METAL FABRICATION BUSINESS CARD

** I will be ending the project and picking design early. This Friday October 3rd at 7am MST if not sooner**
ONE SIDED BUSINESS CARD ONLY. AND LOGO SIZE TO BE DOMINANT so it stands out.
Looking for a black background and will be doing raised chrome/silver font on the business cards. Looking to have the following on the front of the business card. Company logo is uploaded in files.
Company logo
*Compartment Doors
*Roof Radius Metal
*J-Wrap Metal Skirting
*S-Lock Beltline Molding
*Pre-Bent Molding
and more...
Owen Baskell 406.529.1847 info@Trelvo-Works.com
Updates
One sided business card only please. Also logo size should be dominant and sized bigger
Contact Information for Business Card
Black background, Text will be raised chrome/silver, and corners will be rounded.

```html
<!DOCTYPE html>
<html lang="en">
<head>
<meta charset="utf-8">
<title>Trelvo-Works Business Card</title>
<link rel="stylesheet" href="https://fonts.googleapis.com/css2?family=Open+Sans:wght@400;600;700&display=swap">
<style>
  :root {
    --page-bg: #1c1c1c;
    --card-bg: #000000;
    --silver-light: #f2f2f2;
    --silver-mid: #c9c9c9;
    --silver-dark: #8a8a8a;
    --rule: #ffffff;
  }
  html, body {
    margin: 0;
    padding: 0;
    width: 1200px;
    height: 1059px;
    overflow: hidden;
    background: var(--page-bg);
    font-family: "Open Sans", Arial, sans-serif;
  }
  .card {
    position: absolute;
    left: 50px;
    top: 216px;
    width: 1100px;
    height: 627px;
    background: var(--card-bg);
    border-radius: 40px;
    box-shadow: 0 10px 30px rgba(0,0,0,0.6);
  }
  .services {
    position: absolute;
    left: 63px;
    top: 100px;
    margin: 0;
    padding: 0;
    list-style: none;
    font-weight: 600;
    font-size: 28px;
    line-height: 41.5px;
    color: var(--silver-light);
  }
  .services li::before {
    content: "\2022";
    display: inline-block;
    width: 20px;
  }
  .services li:nth-child(4) { color: var(--silver-mid); }
  .services li:nth-child(5) { color: var(--silver-dark); }
  .services .more::before { content: ""; }
  .services .more { padding-left: 4px; color: var(--silver-light); }
  .brand {
    position: absolute;
    left: 530px;
    top: 150px;
    width: 500px;
    display: flex;
    align-items: center;
    gap: 16px;
  }
  .brand-dot {
    width: 30px;
    height: 30px;
    border-radius: 50%;
    background: var(--silver-mid);
    flex: none;
  }
  .brand-name {
    font-weight: 700;
    font-size: 58px;
    color: var(--silver-mid);
    letter-spacing: -0.5px;
    white-space: nowrap;
  }
  .person-name {
    position: absolute;
    left: 63px;
    top: 445px;
    margin: 0;
    font-weight: 600;
    font-size: 40px;
    color: var(--silver-mid);
  }
  .rule {
    position: absolute;
    left: 63px;
    top: 517px;
    width: 963px;
    height: 4px;
    background: var(--rule);
  }
  .contact {
    position: absolute;
    top: 555px;
    display: flex;
    align-items: center;
    gap: 14px;
    font-weight: 400;
    font-size: 26px;
    color: var(--silver-mid);
  }
  .contact-phone { left: 63px; }
  .contact-email { right: 74px; }
  .contact svg { fill: var(--silver-mid); }
</style>
</head>
<body>
  <div class="card">
    <ul class="services">
      <li>Compartment Doors</li>
      <li>Roof Radius Metal</li>
      <li>J-Wrap Metal Skirting</li>
      <li>S-Lock Beltline Molding</li>
      <li>Pre-Bent Molding</li>
      <li class="more">and more...</li>
    </ul>

    <div class="brand">
      <span class="brand-dot"></span>
      <span class="brand-name">Trelvo-Works</span>
    </div>

    <h1 class="person-name">Owen Baskell</h1>
    <div class="rule"></div>

    <div class="contact contact-phone">
      <svg width="26" height="26" viewBox="0 0 24 24" aria-hidden="true">
        <path d="M6.6 10.8a15.1 15.1 0 0 0 6.6 6.6l2.2-2.2a1 1 0 0 1 1-.25 11.4 11.4 0 0 0 3.6.57 1 1 0 0 1 1 1V20a1 1 0 0 1-1 1A17 17 0 0 1 3 4a1 1 0 0 1 1-1h3.5a1 1 0 0 1 1 1c0 1.25.2 2.45.57 3.57a1 1 0 0 1-.25 1z"/>
      </svg>
      <span>406.529.1847</span>
    </div>

    <div class="contact contact-email">
      <svg width="28" height="20" viewBox="0 0 28 20" aria-hidden="true">
        <path d="M0 0h28v3L14 11 0 3z"/>
        <path d="M0 6l14 8 14-8v14H0z"/>
      </svg>
      <span>info@Trelvo-Works.com</span>
    </div>
  </div>
</body>
</html>
```